Broschüre in Querformat für Immobilienmakler
Zielgruppe
Immobilienmakler - Überregional tätig - zielgerichtete Vermarktung - Zielgruppe sind Verkäufer oft ältere Menschen
Ich möchte eine Broschüre mit 12 Seiten im Querformat - Die Broschüre sollte der Website harvrenk-immobilien.example ein wenig ähneln.
Aufgabenstellung
klare Linie - schnell erklärbar und übersichtlich - logischer Aufbau - Aufmerksamkeit erwecken durch Bilder - schnelle Info für Querleser - VERTRAUEN - ehrlich und authentisch - nicht Eitel - schnelle Zurechtfindung - Serviceorientiert - Rundumsorglos Paket

```html
<!DOCTYPE html>
<html lang="de">
<head>
<meta charset="utf-8">
<title>Checkliste Immobilienverkauf – Harvrenk Immobilien</title>
<link rel="stylesheet" href="https://fonts.googleapis.com/css2?family=Montserrat:wght@600;700;800&display=swap">
<style>
  :root {
    --gold: #f9b000;
    --navy: #16213e;
    --paper: #ffffff;
    --lattice: #fdf6e3;
    --frame: #9a9a9a;
  }
  html, body {
    margin: 0;
    padding: 0;
    width: 1200px;
    height: 854px;
    overflow: hidden;
    background: var(--paper);
  }
  .page {
    position: relative;
    width: 1200px;
    height: 854px;
    box-sizing: border-box;
    border: 1px solid var(--frame);
    overflow: hidden;
    font-family: "Montserrat", Arial, sans-serif;
    color: var(--navy);
  }
  .backdrop-pattern {
    position: absolute;
    left: 0;
    top: 0;
    width: 590px;
    height: 854px;
    background: linear-gradient(135deg, var(--lattice), #fffdf7 60%, var(--lattice));
  }
  .rings {
    position: absolute;
    inset: 0;
  }
  .portrait {
    position: absolute;
    border-radius: 50%;
    border: 10px solid var(--gold);
    box-sizing: border-box;
    background: linear-gradient(160deg, #e9e6e1, #b9b3aa 70%, #3c3f4c);
  }
  .portrait--first { left: 84px; top: 151px; width: 200px; height: 200px; }
  .portrait--second { left: 334px; top: 460px; width: 204px; height: 204px; }
  .contact {
    position: absolute;
    line-height: 1.25;
  }
  .contact__name {
    margin: 0;
    font-size: 23px;
    font-weight: 800;
    color: var(--gold);
  }
  .contact__line {
    margin: 0;
    font-size: 11.5px;
    font-weight: 700;
    color: var(--navy);
  }
  .contact--first { right: 664px; top: 229px; text-align: right; }
  .contact--second { left: 73px; top: 532px; text-align: left; }
  .checklist {
    position: absolute;
    left: 665px;
    top: 165px;
    width: 400px;
  }
  .checklist__title {
    margin: 0 0 75px;
    font-size: 23px;
    font-weight: 700;
    line-height: 1.2;
  }
  .checklist__items {
    list-style: none;
    margin: 0;
    padding: 0;
  }
  .checklist__items li {
    position: relative;
    padding-left: 35px;
    font-size: 17.5px;
    font-weight: 600;
    line-height: 24px;
  }
  .checklist__items li::before {
    content: "-";
    position: absolute;
    left: 0;
  }
</style>
</head>
<body>
<main class="page">
  <div class="backdrop-pattern" role="img" aria-label="Dezentes helles Rautenmuster im Hintergrund"></div>

  <svg class="rings" width="1200" height="854" viewBox="0 0 1200 854" aria-hidden="true">
    <path d="M 848 -20 C 890 260, 1010 440, 1215 560" fill="none" stroke="var(--gold)" stroke-width="40"/>
    <circle cx="1288" cy="616" r="240" fill="none" stroke="var(--gold)" stroke-width="32"/>
  </svg>

  <div class="portrait portrait--first" role="img" aria-label="Porträtfoto Jonas Harvrenk"></div>
  <div class="contact contact--first">
    <p class="contact__name">Jonas Harvrenk</p>
    <p class="contact__line">jonas@harvrenk-immobilien.example</p>
    <p class="contact__line">Tel: (0431) 555 20 48</p>
  </div>

  <div class="portrait portrait--second" role="img" aria-label="Porträtfoto Frieda Tervoort"></div>
  <div class="contact contact--second">
    <p class="contact__name">Frieda Tervoort</p>
    <p class="contact__line">frieda@harvrenk-immobilien.example</p>
    <p class="contact__line">Tel: (0151) 555 72 406</p>
  </div>

  <section class="checklist">
    <h1 class="checklist__title">Checkliste Immobilienverkauf –<br>Unterlagen</h1>
    <ul class="checklist__items">
      <li>Grundrisse</li>
      <li>Schnitt und Ansichten</li>
      <li>Wohnflächenberechnung</li>
      <li>Berechnung umbauter Raum m³</li>
      <li>Grundbuchauszug</li>
      <li>Liegenschaftskarte</li>
      <li>Nachweis einer Versicherung (Feuer)</li>
      <li>Personalausweis Verkäufer</li>
      <li>Baubeschreibung</li>
      <li>Energiekosten der letzten 3 Jahre</li>
      <li>Teilungserklärung</li>
      <li>Mietverträge</li>
      <li>Wirtschaftspläne 3 Jahre</li>
      <li>Hausgeldabrechnungen 3 Jahre</li>
      <li>Renovierungen der letzten 20 Jahre</li>
    </ul>
  </section>
</main>
</body>
</html>
```